Personal development products that change your life

This is a direct selling business that sells personal development courses, but also sells the business as well if desired. This is not MLM, and there is no handling of the product required, nor hassling friends or family. We are looking for business minded people wanting to work their own hours and achieve a desirable income from this. A success image or happy image on a flyer would be great. I'd like the website address to be displayed as well thanks. www.gainpath-hub.com.au

Target Market(s)

Business-minded individuals searching for more finances. Self motivated, driven, interested in self development.

Industry/Entity Type

Business

Font styles to use
Sans Serif

Requirements
Must have
• Are you looking for
• - a franchise or business?
• - a change of career?
• - a back up income?
• Not MLM
• No product handling or shipping
• No hard sales required
• website: www.gainpath-hub.com.au
Nice to have
• A picture or background of excited person jumping in the air, or some similar.
• Worded to enrol people interested in achieving more financial headway, or flexible hours, or travel and do this business from anywhere in the world.
• Only need access to a phone, internet connection and a desire to succeed.

```html
<!DOCTYPE html>
<html lang="en">
<head>
<meta charset="utf-8">
<title>Gain and Grow Flyer</title>
<link rel="stylesheet" href="https://fonts.googleapis.com/css2?family=Anton&family=Open+Sans:wght@400&family=Arimo:wght@400&display=swap">
<style>
  :root {
    --red: #f2232d;
    --red-band: #f53a3f;
    --red-deep: #cf0a1c;
    --red-footer: #e8202a;
    --red-dark-text: #b3121c;
    --white: #ffffff;
    --sun-light: #ffd24a;
    --sun-mid: #f29a12;
    --sun-deep: #b85a05;
    --rule: #d9262f;
  }
  * { margin: 0; padding: 0; box-sizing: border-box; }
  html, body { width: 845px; height: 1200px; overflow: hidden; background: var(--white); }
  .flyer { position: relative; width: 845px; height: 1200px; overflow: hidden; background: var(--white); }

  .title {
    position: absolute; top: 8px; left: 0; width: 100%;
    text-align: center; font-family: "Anton", sans-serif; font-weight: 400;
    font-size: 110px; line-height: 1.1; color: var(--red); letter-spacing: 1px;
    white-space: nowrap;
  }
  .tagline {
    position: absolute; top: 138px; left: 0; width: 100%; height: 71px;
    background: var(--red-band); color: var(--white);
    font-family: "Open Sans", sans-serif; font-size: 42px; line-height: 71px;
    padding-left: 90px; white-space: nowrap;
  }
  .hero {
    position: absolute; top: 209px; left: 0; width: 100%; height: 376px;
    background:
      radial-gradient(ellipse 260px 180px at 120px 190px, var(--sun-light) 0%, rgba(255,210,74,0) 70%),
      linear-gradient(180deg, var(--sun-deep) 0%, var(--sun-mid) 45%, #e3860c 70%, #c46a08 100%);
  }

  .tab-list { position: absolute; left: 0; list-style: none; }
  .tab-list li { position: relative; height: 38px; margin-bottom: 22px; }
  .tab-list li::before {
    content: ""; position: absolute; left: 0; top: -11px; width: 72px; height: 60px; background: var(--red);
  }
  .tab-list li:first-child::before { top: 0; height: 49px; }
  .tab-list li:last-child::before { height: 49px; }
  .tab-label {
    position: absolute; left: 69px; top: 0; height: 38px; white-space: nowrap;
    background: var(--red-deep); color: var(--white);
    font-family: "Open Sans", sans-serif; font-size: 27px; line-height: 38px;
    padding: 0 12px 0 22px; border-radius: 0 10px 10px 0;
  }
  .questions { top: 278px; }
  .benefits { top: 778px; }

  .ability-heading {
    position: absolute; top: 596px; width: 100%; text-align: center;
    font-family: "Arimo", sans-serif; font-size: 24px; color: var(--red-dark-text);
  }
  .rule { position: absolute; left: 0; width: 100%; height: 2px; background: var(--rule); }
  .rule-top { top: 641px; }
  .rule-bottom { top: 692px; }
  .ability-text {
    position: absolute; top: 651px; width: 100%; text-align: center;
    font-family: "Arimo", sans-serif; font-size: 22px; color: var(--red-dark-text);
    white-space: nowrap;
  }

  .call {
    position: absolute; top: 1080px; left: 0; width: 100%; height: 59px;
    background: var(--red-band); color: var(--white); text-align: center;
    font-family: "Open Sans", sans-serif; font-size: 30px; line-height: 59px;
  }
  .website {
    position: absolute; top: 1142px; left: 0; width: 100%; height: 58px;
    background: var(--red-footer); color: var(--white); text-align: center;
    font-family: "Arimo", sans-serif; font-size: 27px; line-height: 58px;
  }
</style>
</head>
<body>
<main class="flyer">
  <h1 class="title">GAIN AND GROW</h1>
  <p class="tagline">Start the life you always wanted</p>

  <div class="hero" role="img" aria-label="Silhouette of a person leaping with arms raised against a golden sunset sky"></div>

  <ul class="tab-list questions">
    <li><span class="tab-label">Are you looking for</span></li>
    <li><span class="tab-label">A franchise or business?</span></li>
    <li><span class="tab-label">A change of career?</span></li>
    <li><span class="tab-label">A back up income?</span></li>
  </ul>

  <p class="ability-heading">What makes you able for this?</p>
  <div class="rule rule-top"></div>
  <p class="ability-text">You need access to a phone, internet connection and a desire to succeed.</p>
  <div class="rule rule-bottom"></div>

  <ul class="tab-list benefits">
    <li><span class="tab-label">Your Benifits</span></li>
    <li><span class="tab-label">Not MLM</span></li>
    <li><span class="tab-label">No hard sales required</span></li>
    <li><span class="tab-label">No product handling and shipping</span></li>
  </ul>

  <p class="call">Vist today</p>
  <p class="website">website: www.gainpath-hub.com.au</p>
</main>
</body>
</html>
```